Church Rivers of Morning Gospel Booklet Design

We need a booklet designed that we will be printing to hand out in our community. Wording for each page will be provided and we need graphic design to produce the layouts in a format ready for print. Booklet will be 4.75" x 4.75" square and a total of 12 pages: 1 cover page front, 1 cover page back, 10 inside pages some of which will be full spread across 2 pages.

Target Market(s)

English speaking Westerners

Industry/Entity Type

Religious

Font styles to use
Serif

Colors
ffffff
85abd2
0292cd
33b8a4
5c5c5c

Requirements
Must have
• Minimalist design with clean look described in attached document
Nice to have
• Aesthetically pleasing graphics, crisp fonts, excellent turn around times
Should not have
• Effeminate design, busy look with too much graphic and text

```html
<!DOCTYPE html>
<html lang="en">
<head>
<meta charset="utf-8">
<title>Rivers of Morning — Booklet Cover</title>
<link rel="stylesheet" href="https://fonts.googleapis.com/css2?family=Playfair+Display+SC:wght@400&display=swap">
<style>
  :root {
    --paper: #ffffff;
    --title-blue: #0292cd;
    --vine-teal: #33b8a4;
    --vine-teal-soft: rgba(51, 184, 164, 0.35);
    --ink-grey: #5c5c5c;
  }
  html, body {
    margin: 0;
    padding: 0;
    width: 1200px;
    height: 1200px;
    overflow: hidden;
    background: var(--paper);
  }
  .cover {
    position: relative;
    width: 1200px;
    height: 1200px;
    background: var(--paper);
  }
  .corner-flourish {
    position: absolute;
    width: 180px;
    height: 166px;
    border-radius: 50%;
    background: radial-gradient(circle at center, var(--vine-teal-soft), rgba(51, 184, 164, 0.12) 70%, rgba(51, 184, 164, 0) 100%);
  }
  .corner-flourish--top-left     { left: 178px; top: 172px; }
  .corner-flourish--top-right    { left: 835px; top: 172px; }
  .corner-flourish--bottom-left  { left: 178px; top: 837px; }
  .corner-flourish--bottom-right { left: 835px; top: 837px; }

  .cover-title {
    position: absolute;
    left: 0;
    right: 0;
    top: 0;
    margin: 0;
    font-family: "Playfair Display SC", "Playfair Display", Georgia, serif;
    font-weight: 400;
    color: var(--title-blue);
    text-align: center;
    font-size: 128px;
    line-height: 1;
    letter-spacing: 0.04em;
  }
  .cover-title__line {
    position: absolute;
    left: 22px;
    right: 0;
    white-space: nowrap;
  }
  .cover-title__line--first  { top: 447px; }
  .cover-title__line--second { top: 587px; }
</style>
</head>
<body>
  <main class="cover">
    <div class="corner-flourish corner-flourish--top-left" role="img" aria-label="Teal leafy vine flourish ornament"></div>
    <div class="corner-flourish corner-flourish--top-right" role="img" aria-label="Teal leafy vine flourish ornament"></div>
    <div class="corner-flourish corner-flourish--bottom-left" role="img" aria-label="Teal leafy vine flourish ornament"></div>
    <div class="corner-flourish corner-flourish--bottom-right" role="img" aria-label="Teal leafy vine flourish ornament"></div>

    <h1 class="cover-title">
      <span class="cover-title__line cover-title__line--first">Rivers</span>
      <span class="cover-title__line cover-title__line--second">of Morning</span>
    </h1>
  </main>
</body>
</html>
```